Plakat-Design
Zielgruppe
Wir bieten Tanzkurse in Salsa, Bachata, Kizomba & Zouk an!
Zielgruppe alle Tanzinteressierten Menschen, bekanntheit steigern und Präsenz zeigen!
Wir bieten in den oben genannten Tänzen mit Spezialisierten internationalen Trainern und Trainerinnen didaktisch & methodisch hochwertige Tanzkurse an.
Wir sind die Führende tanzschuleund in diese Sparte.
Aufgabenstellung
DIN/Maße: Datenblatt im Anhang
Display Roll-Up Classic, 85 cm x 200 cm
Attribute die das Design Repräsentieren sollte:
Professionalität, Eye catcher, Tanz, Bewegung, Dynamik, Jung, Frisch
Es soll edel und farblich harmonisch sein. Keine Chilis, kein Kuban Feeling oder Flamenco-Flair.
Mögliches Bildmaterial ist im Anhang zu finden!
Farbe Logo: #A82068
Weitere verwendete Farben: #0A8694
Ein mitgeliefertes Bild, zeigt mehrere Powder / Aquarell Bilder, ich könnte mir auch etwas in diesem Stil vorstellen, doch dezent!
Inhalte: Bin mir hier leider noch nich abschließend sicher welche Inhalte!
Tanzschule
für Salsa, Bachata, Kizomba & Zouk
Kurse von Anfänger A1 bis Masterclas
Kurse ohne Tanzpartner Buchbar
Flexible Tarife mit Monatlicher Bezahlung
Gratis Schnupperstunde

```html
<!DOCTYPE html>
<html lang="de">
<head>
<meta charset="utf-8">
<title>Tanzschule Ritmo Vivo – Roll-Up</title>
<link rel="stylesheet" href="https://fonts.googleapis.com/css2?family=Barlow+Condensed:wght@300;400;500;600&display=swap">
<style>
  :root {
    --navy: #221e35;
    --magenta: #a82068;
    --white: #ffffff;
    --text-font: "Barlow Condensed", "Arial Narrow", sans-serif;
  }
  * { margin: 0; padding: 0; box-sizing: border-box; }
  html, body { width: 1200px; height: 2825px; overflow: hidden; background: var(--navy); }
  .rollup {
    position: relative; width: 1200px; height: 2825px;
    background: var(--navy); font-family: var(--text-font); color: var(--white);
    overflow: hidden;
  }
  .rollup__shapes { position: absolute; inset: 0; }

  .brand { position: absolute; top: 110px; left: 0; width: 1200px; text-align: center; }
  .brand__name {
    display: inline-flex; align-items: center; gap: 36px;
    font-size: 112px; font-weight: 400; line-height: 1; letter-spacing: 2px; color: var(--white);
  }
  .brand__dot { width: 110px; height: 110px; border-radius: 50%; background: var(--magenta); }
  .brand__styles { margin-top: 18px; font-size: 40px; font-weight: 300; letter-spacing: 1px; padding-right: 140px; }

  .hero { position: absolute; left: 0; top: 0; width: 1200px; }
  .hero__title {
    position: absolute; top: 820px; left: 0; width: 1200px; text-align: center;
    font-size: 140px; font-weight: 500; line-height: 1; color: var(--magenta);
  }
  .hero__rule { position: absolute; left: 307px; width: 605px; height: 3px; background: var(--white); }
  .hero__rule--top { top: 1019px; }
  .hero__rule--bottom { top: 1455px; }
  .hero__styles {
    position: absolute; top: 1037px; left: 0; width: 1200px; list-style: none; text-align: center;
    font-size: 92px; font-weight: 400; line-height: 101px; letter-spacing: 9px; text-transform: uppercase;
  }

  .benefits {
    position: absolute; top: 1808px; left: 187px; list-style: none;
    font-size: 60px; font-weight: 400; line-height: 84px;
  }
  .benefits li { position: relative; padding-left: 46px; }
  .benefits li::before {
    content: ""; position: absolute; left: 0; top: 37px; width: 14px; height: 14px;
    border-radius: 50%; background: var(--white);
  }

  .contact {
    position: absolute; top: 2268px; right: 173px; text-align: right; font-style: normal;
    font-size: 48px; font-weight: 300; line-height: 65px;
  }
  .contact__name { font-weight: 600; }
  .contact__line--mail { margin-top: 22px; }
  .website {
    position: absolute; top: 2626px; right: 173px;
    font-size: 92px; font-weight: 400; line-height: 1; color: var(--magenta); letter-spacing: 1px;
  }
</style>
</head>
<body>
<main class="rollup">
  <svg class="rollup__shapes" width="1200" height="2825" viewBox="0 0 1200 2825">
    <defs>
      <linearGradient id="photoTone" gradientUnits="userSpaceOnUse" x1="0" y1="384" x2="0" y2="1800">
        <stop offset="0" stop-color="#f2eff0"/>
        <stop offset="0.28" stop-color="#ddd5d8"/>
        <stop offset="0.42" stop-color="#8e7a89"/>
        <stop offset="0.5" stop-color="#6b586a"/>
        <stop offset="0.76" stop-color="#6b586a"/>
        <stop offset="0.9" stop-color="#a897a2"/>
        <stop offset="1" stop-color="#d6cdd0"/>
      </linearGradient>
    </defs>
    <polygon class="hero__photo" role="img"
      aria-label="Foto: ein junges Tanzpaar dreht sich barfuß in einem hellen Raum mit großen Fenstern"
      points="0,456 1200,384 1200,1728 0,1800" fill="url(#photoTone)"/>
    <polygon class="benefits__band" points="0,1800 1200,1728 1200,2112 0,2196" fill="var(--magenta)"/>
  </svg>

  <header class="brand">
    <div class="brand__name">Ritmo Vivo<span class="brand__dot"></span></div>
    <p class="brand__styles">Salsa · Bachata · Kizomba</p>
  </header>

  <section class="hero">
    <h1 class="hero__title">TANZSCHULE</h1>
    <div class="hero__rule hero__rule--top"></div>
    <ul class="hero__styles">
      <li>Salsa</li>
      <li>Bachata</li>
      <li>Kizomba</li>
      <li>Zouk</li>
    </ul>
    <div class="hero__rule hero__rule--bottom"></div>
  </section>

  <ul class="benefits">
    <li>Kurse von Anfänger A1 bis Masterclass</li>
    <li>Kurse ohne Tanzpartner buchbar</li>
    <li>Flexible Tarife mit monatlicher Bezahlung</li>
    <li>Gratis Schnupperstunde</li>
  </ul>

  <address class="contact">
    <p class="contact__name">Tanzschule Ritmo Vivo</p>
    <p class="contact__line">Lindenweg 14 &amp; weitere Locations</p>
    <p class="contact__line">79100 Talheim am See</p>
    <p class="contact__line contact__line--mail">info@ritmo-vivo.de | T +49 150 000 482 16</p>
  </address>

  <p class="website">WWW.RITMO-VIVO.DE</p>
</main>
</body>
</html>
```